shopfitters cards and stationery
Stationery
Project: shopfitters cards and stationery
shopfitters cards and stationery  - Construction
Creative Brief
Professional
Mark Pelling
Contracts Manager
7/24 Quarry Lane Wendale 4182
mark@fitwrightgroup.com.au
www.fitwrightgroup.com.au
Phone numbers and other details etc will change if you could use them for know that will be great. give me your best work :) Thanks

```html
<!DOCTYPE html>
<html lang="en">
<head>
<meta charset="utf-8">
<title>Fitwright Group – Business Card</title>
<link rel="stylesheet" href="https://fonts.googleapis.com/css2?family=Michroma&display=swap">
<style>
  :root {
    --backdrop: #e9e6e1;
    --card: #ffffff;
    --brand-navy: #1e2b5c;
    --brand-blue: #2f56a8;
    --icon-violet: #5a4fae;
    --text-grey: #3c3c44;
    --rule: #d9dbe4;
  }
  html, body {
    margin: 0;
    width: 1200px;
    height: 902px;
    overflow: hidden;
    background: var(--backdrop);
    font-family: "Michroma", sans-serif;
  }
  .card {
    position: absolute;
    left: 150px;
    top: 201px;
    width: 900px;
    height: 500px;
    background: var(--card);
    box-shadow: 0 12px 30px rgba(0,0,0,0.18);
  }
  .brand {
    position: absolute;
    right: 46px;
    top: 52px;
    display: flex;
    align-items: center;
    gap: 16px;
  }
  .brand-dot {
    width: 66px;
    height: 66px;
    border-radius: 50%;
    background: var(--brand-blue);
  }
  .brand-name {
    font-size: 26px;
    color: var(--brand-navy);
    letter-spacing: 2px;
    line-height: 1;
  }
  .contacts {
    position: absolute;
    right: 46px;
    top: 168px;
    margin: 0;
    padding: 0;
    list-style: none;
    text-align: right;
  }
  .contacts li {
    display: flex;
    justify-content: flex-end;
    align-items: center;
    gap: 10px;
    height: 22px;
    font-size: 12px;
    letter-spacing: 1.5px;
    color: var(--text-grey);
  }
  .contacts .gap { height: 20px; }
  .contacts svg { width: 13px; height: 13px; flex: none; }
  .person {
    position: absolute;
    left: 48px;
    bottom: 58px;
  }
  .person-name {
    margin: 0 0 8px;
    font-size: 16px;
    font-weight: normal;
    color: var(--brand-blue);
    letter-spacing: 2px;
  }
  .person-role {
    margin: 0;
    padding-top: 6px;
    border-top: 1px solid var(--rule);
    font-size: 12px;
    color: var(--text-grey);
    letter-spacing: 1.5px;
  }
</style>
</head>
<body>
  <main class="card">
    <div class="brand">
      <span class="brand-dot"></span>
      <span class="brand-name">FITWRIGHT GROUP</span>
    </div>

    <ul class="contacts">
      <li>7/24 Quarry Lane
        <svg viewBox="0 0 14 14"><circle cx="7" cy="7" r="7" fill="var(--icon-violet)"/><path d="M7 3.2a2.4 2.4 0 0 0-2.4 2.4c0 1.8 2.4 4.6 2.4 4.6s2.4-2.8 2.4-4.6A2.4 2.4 0 0 0 7 3.2z" fill="#fff"/></svg>
      </li>
      <li>Wendale 4182
        <svg viewBox="0 0 14 14"><circle cx="7" cy="7" r="7" fill="var(--icon-violet)"/></svg>
      </li>
      <li>07 3162 4870
        <svg viewBox="0 0 14 14"><circle cx="7" cy="7" r="7" fill="var(--icon-violet)"/><path d="M4.6 3.8l1.3-.4.8 1.8-.9.7a5 5 0 0 0 2.3 2.3l.7-.9 1.8.8-.4 1.3c-3 .2-5.8-2.6-5.6-5.6z" fill="#fff"/></svg>
      </li>
      <li>0412 587 309
        <svg viewBox="0 0 14 14"><circle cx="7" cy="7" r="7" fill="var(--icon-violet)"/><rect x="5" y="3.2" width="4" height="7.6" rx=".8" fill="#fff"/></svg>
      </li>
      <li>07 3295 6614
        <svg viewBox="0 0 14 14"><circle cx="7" cy="7" r="7" fill="var(--icon-violet)"/><rect x="4" y="5" width="6" height="4.5" fill="#fff"/></svg>
      </li>
      <li class="gap"></li>
      <li>mark@fitwrightgroup.com.au
        <svg viewBox="0 0 14 14"><circle cx="7" cy="7" r="7" fill="var(--icon-violet)"/><rect x="3.8" y="4.6" width="6.4" height="4.8" fill="#fff"/></svg>
      </li>
      <li>www.fitwrightgroup.com.au
        <svg viewBox="0 0 14 14"><circle cx="7" cy="7" r="7" fill="var(--icon-violet)"/><circle cx="7" cy="7" r="3.2" fill="none" stroke="#fff" stroke-width="1"/></svg>
      </li>
    </ul>

    <div class="person">
      <h1 class="person-name">Mark Pelling</h1>
      <p class="person-role">Contracts Manager</p>
    </div>
  </main>
</body>
</html>
```